" Atendimento médico em consultório/Clinica para mulheres em geral. A clinica contará com três médicas ginecologistas. Inicialmente somente a Dra. Lívia atenderá. O principal valor da Clinica é com o cuidado com a Mulher através de atendimento individual e cuidadoso através de especialistas nas áreas da ginecologia e Obstetricia. Apesar de possuir atendimento Obstétrico, o mesmo não será o principal foco da clinica. "

```html
<!DOCTYPE html>
<html lang="pt-BR">
<head>
<meta charset="utf-8">
<title>Clínica Dra. Lívia – Cartão verso</title>
<link rel="stylesheet" href="https://fonts.googleapis.com/css2?family=Questrial&family=Arimo:wght@400&display=swap">
<style>
  :root {
    --coral: #ee6a6f;
    --white: #ffffff;
    --ink: #6b6b6b;
    --page: #ffffff;
  }
  * { box-sizing: border-box; margin: 0; padding: 0; }
  html, body {
    width: 1200px; height: 1200px; overflow: hidden;
    background: var(--page);
  }
  .sheet { position: relative; width: 1200px; height: 1200px; }
  .card-coral {
    position: absolute; left: 67px; top: 144px;
    width: 552px; height: 912px;
    background: var(--coral);
  }
  .motif {
    position: absolute; left: 456px; top: 144px;
    width: 520px; height: 912px;
    background: radial-gradient(ellipse at 50% 50%, rgba(255,255,255,0.16) 0%, rgba(255,255,255,0.06) 45%, rgba(255,255,255,0) 70%);
    mix-blend-mode: normal;
  }
  .motif-right {
    position: absolute; left: 619px; top: 144px;
    width: 357px; height: 912px;
    background: radial-gradient(ellipse at 0% 50%, rgba(238,106,111,0.05) 0%, rgba(238,106,111,0.02) 50%, rgba(238,106,111,0) 75%);
  }
  .contacts {
    position: absolute; list-style: none;
    font-family: "Questrial", sans-serif;
    font-size: 25px; letter-spacing: 0.2px;
  }
  .contacts.on-coral { left: 112px; top: 392px; color: var(--white); }
  .contacts.on-white { left: 712px; top: 392px; color: var(--ink); }
  .contact {
    display: flex; align-items: center; gap: 14px;
    height: 56.5px;
  }
  .contact.address { align-items: flex-start; margin-top: 8px; height: auto; }
  .icon { width: 30px; height: 30px; flex: none; }
  .on-coral .icon .disc { fill: var(--white); }
  .on-coral .icon .glyph { fill: var(--coral); }
  .on-white .icon .disc { fill: var(--coral); }
  .on-white .icon .glyph { fill: var(--white); }
  .address-text {
    font-family: "Arimo", sans-serif;
    font-size: 18px; line-height: 21px; letter-spacing: -0.2px;
    margin-top: -2px;
  }
</style>
</head>
<body>
<div class="sheet">
  <div class="card-coral"></div>
  <div class="motif" role="img" aria-label="Ilustração em traço fino de silhueta de gestante, decoração de fundo"></div>
  <div class="motif-right" role="img" aria-label="Continuação da ilustração em traço fino de gestante"></div>

  <ul class="contacts on-coral">
    <li class="contact"><svg class="icon" viewBox="0 0 30 30"><circle class="disc" cx="15" cy="15" r="15"/><path class="glyph" d="M10.5 8.5l3 0 1 4-2 1.3c.8 1.8 2 3 3.7 3.7l1.3-2 4 1v3c0 .8-.7 1.5-1.5 1.5C13.5 21 9 16.5 9 10c0-.8.7-1.5 1.5-1.5z"/></svg><span>(19) 3400-1520 / 3400-1521</span></li>
    <li class="contact"><svg class="icon" viewBox="0 0 30 30"><circle class="disc" cx="15" cy="15" r="15"/></svg><span>(19) 98100-4477</span></li>
    <li class="contact"><svg class="icon" viewBox="0 0 30 30"><circle class="disc" cx="15" cy="15" r="15"/><path class="glyph" d="M8 10h14v10H8z M8.5 10.5l6.5 5 6.5-5" /></svg><span>contato@clinicalivia.com</span></li>
    <li class="contact"><svg class="icon" viewBox="0 0 30 30"><circle class="disc" cx="15" cy="15" r="15"/></svg><span>social.com/clinicalivia</span></li>
    <li class="contact"><svg class="icon" viewBox="0 0 30 30"><circle class="disc" cx="15" cy="15" r="15"/></svg><span>@clinicalivia</span></li>
    <li class="contact"><svg class="icon" viewBox="0 0 30 30"><circle class="disc" cx="15" cy="15" r="15"/></svg><span>@clinicalivia</span></li>
    <li class="contact"><svg class="icon" viewBox="0 0 30 30"><circle class="disc" cx="15" cy="15" r="15"/><circle class="glyph" cx="15" cy="15" r="7"/></svg><span>www.clinicalivia.com.br</span></li>
    <li class="contact address"><svg class="icon" viewBox="0 0 30 30"><circle class="disc" cx="15" cy="15" r="15"/><path class="glyph" d="M15 7a5.5 5.5 0 0 0-5.5 5.5C9.5 17 15 23 15 23s5.5-6 5.5-10.5A5.5 5.5 0 0 0 15 7zm0 7.8a2.3 2.3 0 1 1 0-4.6 2.3 2.3 0 0 1 0 4.6z"/></svg><span class="address-text">Rua das Acácias, 415 3º Andar Sala 12<br>Jd. Aurora Ed. Centro Médico Aurora<br>13050-220 Campinas-SP</span></li>
  </ul>

  <ul class="contacts on-white">
    <li class="contact"><svg class="icon" viewBox="0 0 30 30"><circle class="disc" cx="15" cy="15" r="15"/><path class="glyph" d="M10.5 8.5l3 0 1 4-2 1.3c.8 1.8 2 3 3.7 3.7l1.3-2 4 1v3c0 .8-.7 1.5-1.5 1.5C13.5 21 9 16.5 9 10c0-.8.7-1.5 1.5-1.5z"/></svg><span>(19) 3400-1520 / 3400-1521</span></li>
    <li class="contact"><svg class="icon" viewBox="0 0 30 30"><circle class="disc" cx="15" cy="15" r="15"/></svg><span>(19) 98100-4477</span></li>
    <li class="contact"><svg class="icon" viewBox="0 0 30 30"><circle class="disc" cx="15" cy="15" r="15"/><path class="glyph" d="M8 10h14v10H8z M8.5 10.5l6.5 5 6.5-5" /></svg><span>contato@clinicalivia.com</span></li>
    <li class="contact"><svg class="icon" viewBox="0 0 30 30"><circle class="disc" cx="15" cy="15" r="15"/></svg><span>social.com/clinicalivia</span></li>
    <li class="contact"><svg class="icon" viewBox="0 0 30 30"><circle class="disc" cx="15" cy="15" r="15"/></svg><span>@clinicalivia</span></li>
    <li class="contact"><svg class="icon" viewBox="0 0 30 30"><circle class="disc" cx="15" cy="15" r="15"/></svg><span>@clinicalivia</span></li>
    <li class="contact"><svg class="icon" viewBox="0 0 30 30"><circle class="disc" cx="15" cy="15" r="15"/><circle class="glyph" cx="15" cy="15" r="7"/></svg><span>www.clinicalivia.com.br</span></li>
    <li class="contact address"><svg class="icon" viewBox="0 0 30 30"><circle class="disc" cx="15" cy="15" r="15"/><path class="glyph" d="M15 7a5.5 5.5 0 0 0-5.5 5.5C9.5 17 15 23 15 23s5.5-6 5.5-10.5A5.5 5.5 0 0 0 15 7zm0 7.8a2.3 2.3 0 1 1 0-4.6 2.3 2.3 0 0 1 0 4.6z"/></svg><span class="address-text">Rua das Acácias, 415 3º Andar Sala 12<br>Jd. Aurora Ed. Centro Médico Aurora<br>13050-220 Campinas-SP</span></li>
  </ul>
</div>
</body>
</html>
```